Professional/modern business card design for construction company

We need a new business card design, double sided keeping it modern, sleek, professional and simple. We are an earthmoving business but do not want any pictures of machinery. I would like one side to have the logo and the other to have all the information, keeping with the colors in our logo. The business card will need to be able to be customised so we can use it for several different managers., we would also like to be able to use the design to apply it to other stationary ie. letterheads, notebooks etc. We do not really have a tag line but we could put on there that we specialise in - Agriculture, Civil Construction and Mining.

Contact Information for Business Card

Balgo Groundworks Pty Ltd
ABN 58 402 917 364
82 Dunmore Creek Road, Wirralee NSW 2461

Desmond Fairweather
Managing Director
P 0438 614 205
E desfairweather@balgogroundworks.com.au

Font styles to use
Serif
Sans Serif

Requirements
Nice to have
• I have attached some examples of ideas.
Should not have
• images of machinery

```html
<!DOCTYPE html>
<html lang="en">
<head>
<meta charset="utf-8">
<title>Balgo Groundworks – Business Card</title>
<link href="https://fonts.googleapis.com/css2?family=Roboto:wght@400;700;900&display=swap" rel="stylesheet">
<style>
  :root {
    --stage: #4a4b4f;
    --card: #242424;
    --card-edge: #1c1c1c;
    --orange: #f5891f;
    --text-grey: #b4b4b4;
    --logo-emboss: #161616;
  }
  * { margin: 0; padding: 0; box-sizing: border-box; }
  html, body { width: 1200px; height: 1200px; overflow: hidden; }
  body {
    background: var(--stage);
    font-family: "Roboto", Arial, sans-serif;
    position: relative;
  }
  .card {
    position: absolute;
    left: 250px;
    width: 700px;
    height: 400px;
    border-radius: 26px;
    background: linear-gradient(135deg, #282828, var(--card-edge));
    overflow: hidden;
    box-shadow: 0 18px 40px rgba(0,0,0,.35);
  }
  .card--front { top: 150px; }
  .card--back { top: 630px; }

  /* Logo side */
  .brand-emboss {
    position: absolute;
    inset: 0;
    display: flex;
    align-items: center;
    justify-content: center;
  }
  .brand-emboss__name {
    font-weight: 900;
    font-size: 44px;
    letter-spacing: 2px;
    color: var(--logo-emboss);
    text-transform: uppercase;
    text-align: center;
    line-height: 1.1;
  }

  /* Info side */
  .brand {
    position: absolute;
    top: 78px;
    right: 60px;
    text-align: right;
    font-weight: 900;
    font-size: 30px;
    line-height: 1.1;
    letter-spacing: 1px;
    color: var(--orange);
    text-transform: uppercase;
  }
  .person {
    position: absolute;
    left: 48px;
    top: 168px;
  }
  .person__name {
    font-weight: 900;
    font-size: 24px;
    color: var(--orange);
    text-transform: uppercase;
    letter-spacing: .3px;
  }
  .person__title {
    font-size: 13px;
    color: var(--text-grey);
    margin-top: 2px;
  }
  .company {
    margin-top: 10px;
    font-size: 13px;
    line-height: 1.4;
    color: var(--text-grey);
  }
  .company__name { color: var(--orange); font-weight: 700; }
  .divider {
    position: absolute;
    left: 250px;
    right: 60px;
    top: 232px;
    height: 1px;
    background: var(--orange);
  }
  .contact {
    position: absolute;
    right: 60px;
    top: 268px;
    text-align: right;
    font-size: 15px;
    color: var(--text-grey);
    line-height: 1.7;
  }
  .contact__row { display: flex; align-items: center; justify-content: flex-end; gap: 10px; }
  .contact__row svg { width: 15px; height: 15px; fill: var(--orange); }
  .band {
    position: absolute;
    left: 0; right: 0; bottom: 0;
    height: 20px;
    background: var(--orange);
  }
</style>
</head>
<body>
  <section class="card card--front" aria-label="Card front with company name">
    <div class="brand-emboss">
      <div class="brand-emboss__name">Balgo Groundworks<br>Pty Ltd</div>
    </div>
  </section>

  <section class="card card--back" aria-label="Card back with contact details">
    <div class="brand">Balgo Groundworks<br>Pty Ltd</div>

    <div class="person">
      <div class="person__name">Desmond Fairweather</div>
      <div class="person__title">Managing Director</div>
      <div class="company">
        <div class="company__name">Balgo Groundworks Pty Ltd</div>
        <div>ABN 58 402 917 364</div>
        <div>82 Dunmore Creek Road, Wirralee NSW 2461</div>
      </div>
    </div>

    <div class="divider"></div>

    <div class="contact">
      <div class="contact__row">0438 614 205
        <svg viewBox="0 0 24 24" aria-hidden="true"><path d="M6.6 10.8a15.1 15.1 0 0 0 6.6 6.6l2.2-2.2c.3-.3.7-.4 1-.2 1.1.4 2.3.6 3.6.6.6 0 1 .4 1 1V20c0 .6-.4 1-1 1A17 17 0 0 1 3 4c0-.6.4-1 1-1h3.5c.6 0 1 .4 1 1 0 1.3.2 2.5.6 3.6.1.3 0 .7-.2 1z"/></svg>
      </div>
      <div class="contact__row">desfairweather@balgogroundworks.com.au
        <svg viewBox="0 0 24 24" aria-hidden="true"><path d="M3 5h18c.6 0 1 .4 1 1v12c0 .6-.4 1-1 1H3c-.6 0-1-.4-1-1V6c0-.6.4-1 1-1zm9 7.5L20 7H4z"/></svg>
      </div>
    </div>

    <div class="band"></div>
  </section>
</body>
</html>
```